Business card for IT company

Looking for a business card for an IT company providing server, network, and application support to medium businesses. Company name is Halvern Systems. Website is www.halvernsystems.example, would like to use the green color that is on the homepage. Prefer design to be done in Illustrator. Please, only DESIGNERS apply - no PHP programmers attempting to do design. Thank you

Industry/Entity Type

Information Technology

Requirements
Must have
• Green
Should not have
• Template designs, or designs done by non-designer type people

```html
<!DOCTYPE html>
<html lang="en">
<head>
<meta charset="utf-8">
<title>Halvern Systems – Business Card</title>
<link rel="stylesheet" href="https://fonts.googleapis.com/css2?family=Roboto:wght@300;400;700&display=swap">
<style>
  :root {
    --stage: #3b3b3b;
    --brand-green: #76a334;
    --paper: #ffffff;
    --ink-grey: #555555;
  }
  html, body {
    margin: 0;
    padding: 0;
    width: 1105px;
    height: 1200px;
    overflow: hidden;
    background: var(--stage);
    font-family: "Roboto", Arial, sans-serif;
  }
  .canvas {
    position: relative;
    width: 1105px;
    height: 1200px;
  }
  .card {
    position: absolute;
    left: 196px;
    width: 720px;
    height: 412px;
    border-radius: 19px;
    background: var(--brand-green);
    overflow: hidden;
  }
  .card--front { top: 145px; }
  .card--back { top: 602px; }

  .contact-disc {
    position: absolute;
    left: 155px;
    top: 0;
    width: 414px;
    height: 414px;
    margin-top: -2px;
    border-radius: 50%;
    background: var(--paper);
  }
  .contact {
    position: absolute;
    left: 0;
    right: 0;
    top: 208px;
    text-align: center;
    color: var(--ink-grey);
  }
  .contact__place {
    margin: 0;
    font-size: 23px;
    font-weight: 700;
    color: var(--brand-green);
    line-height: 28px;
  }
  .contact__region {
    margin: 2px 0 0;
    font-size: 18px;
    line-height: 24px;
  }
  .contact__phone {
    margin: 12px 0 0;
    font-size: 18px;
    line-height: 24px;
  }
  .contact__phone-label {
    color: var(--brand-green);
    font-weight: 700;
  }
  .contact__line {
    margin: 4px 0 0;
    font-size: 17px;
    line-height: 24px;
  }

  .brand-disc {
    position: absolute;
    left: 278px;
    top: 73px;
    width: 166px;
    height: 166px;
    border-radius: 50%;
    background: var(--paper);
  }
  .brand-name {
    position: absolute;
    left: 0;
    right: 0;
    top: 274px;
    margin: 0;
    text-align: center;
    color: var(--paper);
    font-size: 34px;
    font-weight: 300;
    letter-spacing: 3px;
    text-transform: uppercase;
  }
</style>
</head>
<body>
<main class="canvas">
  <section class="card card--front" aria-label="Card front">
    <div class="contact-disc">
      <div class="contact">
        <p class="contact__place">Alder Ridge</p>
        <p class="contact__region">Westmarch</p>
        <p class="contact__phone"><span class="contact__phone-label">P:</span> 555.014.2270</p>
        <p class="contact__line">support@halvernsystems.example</p>
        <p class="contact__line">www.halvernsystems.example</p>
      </div>
    </div>
  </section>

  <section class="card card--back" aria-label="Card back">
    <div class="brand-disc"></div>
    <p class="brand-name">Halvern Systems</p>
  </section>
</main>
</body>
</html>
```